CRPG is needing business cards, and stationary created.

Pixel Forge created a logo for our business, and now we are wanting business cards, and stationary. I have included two designs of the same logo. Please feel free to use them as you want. The name of the company is Cedar Ridge Property Group LLC, the address is 812 NE Willow Ln., Suite 9, the city & state is Bend, Oregon, zip code is 97815, Telephone number is 541-327-4489, Fax number is 541-327-6051, the name on the business card is Carl Whitby CMCA

Industry/Entity Type

Property Management

Contact Information for Business Card

The card needs to look professional. Upscale.

Requirements
Must have
• The colors we are using are on the logo that has been uploaded.

```html
<!DOCTYPE html>
<html lang="en">
<head>
<meta charset="utf-8">
<title>Cedar Ridge Property Group — Business Cards</title>
<link href="https://fonts.googleapis.com/css2?family=Arimo:wght@400;700&display=swap" rel="stylesheet">
<style>
  :root {
    --teal: #3a9c88;
    --teal-light: #5aab99;
    --slate: #4a5260;
    --ink: #2e3138;
    --muted: #6b7280;
    --paper: #ffffff;
    --backdrop: #e0e0e0;
  }
  * { box-sizing: border-box; margin: 0; padding: 0; }
  html, body { width: 1200px; height: 1200px; overflow: hidden; }
  body { background: var(--backdrop); position: relative; font-family: "Arimo", Arial, sans-serif; }

  .card {
    position: absolute; left: 180px; width: 840px; height: 480px;
    border-radius: 4px; box-shadow: 0 12px 30px rgba(0,0,0,.12);
  }
  .card--front { top: 90px; background: linear-gradient(135deg, var(--teal) 0%, var(--teal-light) 100%); }
  .card--back { top: 630px; background: var(--paper); }

  .brand { position: absolute; display: flex; align-items: center; font-family: "Arimo", Arial, sans-serif; font-weight: 700; }
  .brand__mark { flex: none; }
  .brand__name { line-height: 1.15; }

  .card--front .brand { left: 0; right: 0; top: 0; bottom: 0; justify-content: center; gap: 22px; color: var(--paper); }
  .card--front .brand__mark { width: 48px; height: 48px; background: var(--paper); }
  .card--front .brand__name { font-size: 40px; }

  .card--back .brand { left: 56px; top: 180px; width: 360px; gap: 16px; color: var(--teal); }
  .card--back .brand__mark { width: 40px; height: 40px; background: var(--teal); }
  .card--back .brand__name { font-size: 30px; }

  .contact { position: absolute; left: 470px; top: 130px; color: var(--ink); }
  .contact__name { font-weight: 700; font-size: 26px; }
  .contact__role { font-size: 15px; color: var(--muted); margin: 4px 0 18px; letter-spacing: 1px; }
  .contact__line { display: flex; align-items: center; gap: 10px; font-size: 17px; color: var(--ink); margin-bottom: 8px; }
  .contact__line svg { width: 16px; height: 16px; fill: none; stroke: var(--muted); stroke-width: 2; }
  .contact__address { font-size: 17px; margin-top: 14px; line-height: 1.4; }
</style>
</head>
<body>
  <section class="card card--front">
    <div class="brand">
      <span class="brand__mark"></span>
      <span class="brand__name">Cedar Ridge Property Group</span>
    </div>
  </section>

  <section class="card card--back">
    <div class="brand">
      <span class="brand__mark"></span>
      <span class="brand__name">Cedar Ridge<br>Property Group</span>
    </div>

    <div class="contact">
      <div class="contact__name">Carl Whitby, CMCA</div>
      <div class="contact__role">POSITION</div>
      <div class="contact__line">
        <svg viewBox="0 0 24 24"><path d="M5 3h4l2 5-3 2a11 11 0 0 0 6 6l2-3 5 2v4a2 2 0 0 1-2 2A18 18 0 0 1 3 5a2 2 0 0 1 2-2z"/></svg>
        (541) 327-4489
      </div>
      <div class="contact__line">
        <svg viewBox="0 0 24 24"><rect x="6" y="3" width="12" height="6"/><rect x="3" y="9" width="18" height="10" rx="1"/><path d="M7 14h6"/></svg>
        (541) 327-6051
      </div>
      <div class="contact__line">
        <svg viewBox="0 0 24 24"><rect x="3" y="5" width="18" height="14" rx="1"/><path d="M3 6l9 7 9-7"/></svg>
        name@cedarridgepg.com
      </div>
      <div class="contact__line">
        <svg viewBox="0 0 24 24"><path d="M10 14a4 4 0 0 0 6 0l3-3a4 4 0 0 0-6-6l-1 1"/><path d="M14 10a4 4 0 0 0-6 0l-3 3a4 4 0 0 0 6 6l1-1"/></svg>
        www.cedarridgepg.com
      </div>
      <div class="contact__address">812 NE Willow Ln., Suite 9,<br>Bend, Oregon 97815</div>
    </div>
  </section>
</body>
</html>
```